I need a sophisticated and powerful book cover design that combines Japanese minimalism with contemporary appeal. The cover should convey personal transformation through the metaphor of a katana (Japanese sword).
Key Design Elements:
A katana, either partially shown or artistically rendered
Subtle Japanese design elements without being stereotypical
Clean, minimalist aesthetic
Professional font selection that bridges Eastern and Western typography
Color scheme: Deep blacks, steel grays, and possibly a touch of red or gold for accent
Mood/Style:
Professional and sophisticated
Blend of traditional Japanese aesthetics with modern design
Should appeal to personal development and business readers
Must convey strength and transformation
Elegant rather than aggressive
Specific Requirements:
Title: "The Lantern Compass"
Subtitle: "Quiet Practices for Growing Inner Steadiness and Calm Endurance Daily"
Author names: Moheshan Tadeli and Veena Tadeli
Cover dimensions: Standard hardcover book size (6" x 9")
Must work well in both physical and digital thumbnail formats
Should be striking and legible when viewed as a small image online
Design Specifics:
Japanese elements such as brushstroke effects, kanji characters, or wave patterns
The design should reflect the book's core message: personal transformation through Japanese wisdom principles, using the katana as a metaphor for growth and development.
Colors
Look and feel

```html
<!DOCTYPE html>
<html lang="en">
<head>
<meta charset="utf-8">
<title>The Lantern Compass</title>
<link rel="stylesheet" href="https://fonts.googleapis.com/css2?family=Open+Sans:wght@400;600;700&display=swap">
<style>
  :root {
    --ink: #262626;
    --charcoal: #2e2e2e;
    --slate: #3b3b3b;
    --stone: #4a4a4a;
    --tile: #c9c9c7;
    --tile-dark: #a9a9a7;
    --paper: #ffffff;
    --crimson: #c8141b;
    --blood: #7a0c10;
    --steel: #d9dcdf;
  }
  * { margin: 0; padding: 0; box-sizing: border-box; }
  html, body { width: 800px; height: 1200px; overflow: hidden; background: var(--ink); }
  .cover {
    position: relative;
    width: 800px;
    height: 1200px;
    overflow: hidden;
    font-family: "Open Sans", Arial, sans-serif;
    color: var(--paper);
    background: linear-gradient(180deg, #333333 0%, var(--charcoal) 40%, #2a2a2a 55%);
  }
  .ground-tiles {
    position: absolute; left: 0; top: 657px; width: 372px; height: 306px;
    background: linear-gradient(160deg, var(--tile) 0%, var(--tile-dark) 100%);
  }
  .ground-slate {
    position: absolute; left: 372px; top: 657px; width: 428px; height: 306px;
    background: var(--slate);
  }
  .ground-stone {
    position: absolute; left: 0; top: 963px; width: 800px; height: 237px;
    background: linear-gradient(180deg, var(--stone) 0%, #3c3c3c 100%);
  }
  .horizon-line {
    position: absolute; left: 600px; top: 660px; width: 200px; height: 3px;
    background: var(--paper);
  }
  .emblem {
    position: absolute; left: 0; top: 0; width: 800px; height: 1200px;
  }
  .title-block {
    position: absolute; left: 74px; top: 34px; width: 680px;
  }
  .title {
    font-size: 51px; font-weight: 600; line-height: 1.1; letter-spacing: 0.2px;
  }
  .subtitle {
    margin-top: 12px; font-size: 23.5px; font-weight: 400; line-height: 1.3;
  }
  .authors {
    position: absolute; top: 1095px; left: 0; width: 800px;
    font-size: 37px; font-weight: 700;
  }
  .author { position: absolute; white-space: nowrap; }
  .author--first { left: 82px; }
  .author--second { left: 442px; }
</style>
</head>
<body>
  <main class="cover">
    <div class="ground-tiles" role="img" aria-label="Pale grey square tile pattern"></div>
    <div class="ground-slate"></div>
    <div class="ground-stone" role="img" aria-label="Dark grey textured stone surface"></div>
    <div class="horizon-line"></div>

    <svg class="emblem" viewBox="0 0 800 1200" role="img" aria-label="Red and black fan-like circle with an upright katana passing through its centre">
      <defs>
        <radialGradient id="emblem-fill" cx="0.5" cy="0.5" r="0.5">
          <stop offset="0" stop-color="#1a1a1a"/>
          <stop offset="0.35" stop-color="#1a1a1a"/>
          <stop offset="0.55" stop-color="var(--blood)"/>
          <stop offset="1" stop-color="var(--crimson)"/>
        </radialGradient>
        <linearGradient id="blade-fill" x1="0" y1="0" x2="0" y2="1">
          <stop offset="0" stop-color="#1c1c1c"/>
          <stop offset="0.35" stop-color="#555"/>
          <stop offset="0.45" stop-color="var(--steel)"/>
          <stop offset="1" stop-color="#f2f2f2"/>
        </linearGradient>
      </defs>
      <circle cx="398" cy="648" r="231" fill="url(#emblem-fill)"/>
      <rect x="385" y="167" width="26" height="916" rx="6" fill="url(#blade-fill)"/>
    </svg>

    <header class="title-block">
      <h1 class="title">The Lantern Compass</h1>
      <p class="subtitle">Quiet Practices for Growing Inner Steadiness<br>and Calm Endurance Daily</p>
    </header>

    <footer class="authors">
      <span class="author author--first">Moheshan Tadeli</span>
      <span class="author author--second">&amp; Veena Tadeli</span>
    </footer>
  </main>
</body>
</html>
```